Super Greens Label for Supplement Bottle

We want to design a front label for a health supplement bottle. The product is called Meadow Twist Chews™. This will be a new product so there is no current website for the product. The focus is on supergreens that taste great and deliver support for energy, digestion, and immune defense.
We want it to be modern, vibrant and appealing.
Bottle size: standard size supplement CLEAR bottle size, with white child resistant cap and the label panel dimensions are 3” x 7”. The label should be primarily white and green, with a touch of red; (see color palettes)/it can also ONLY be white and green. See samples attached.
We are only focused on the front of the bottle design, not on the back, but leave space for the supplement panel and other text on the back.
So the text for the front of the bottle is:
RT Balden's
Meadow Twist Chews™
Super Greens Blend for:
Energy, Digestion, and Immune Support*
60 Gummies | Dietary Supplement
Raspberry Flavor Gummies
Off to side of the label:
Non-GMO
Vegan Friendly
Plant-Based
Gelatin Free
Colors
Designer to choose colors to be used in the design.

```html
<!DOCTYPE html>
<html lang="en">
<head>
<meta charset="utf-8">
<title>Meadow Twist Chews – Front Label</title>
<link rel="stylesheet" href="https://fonts.googleapis.com/css2?family=Montserrat:wght@800&family=Ubuntu:wght@500;700&family=Oswald:wght@400&display=swap">
<style>
  :root {
    --stage: #8c8c8c;
    --paper: #ffffff;
    --green: #0f7551;
    --green-light: #2a9a6e;
    --green-deep: #0b5e40;
    --ink: #0a0a0a;
    --berry: #d9232d;
    --silver: #c9c9c9;
  }
  * { margin: 0; padding: 0; box-sizing: border-box; }
  html, body { width: 1200px; height: 788px; overflow: hidden; }
  body { background: var(--stage); position: relative; }

  .label {
    position: absolute; left: 270px; top: 30px;
    width: 660px; height: 728px;
    background: var(--paper);
    overflow: hidden;
    box-shadow: 0 2px 6px rgba(0,0,0,.15);
  }

  .brand-name {
    position: absolute; left: 44px; top: 34px;
    font-family: "Ubuntu", sans-serif; font-weight: 700;
    font-size: 22px; line-height: 26px; color: var(--green);
  }

  .product-name {
    position: absolute; left: 40px; top: 66px;
    font-family: "Montserrat", sans-serif; font-weight: 800;
    font-size: 84px; line-height: 84px; letter-spacing: -1px;
    color: var(--green);
  }
  .product-name span { display: block; }
  .product-name .dark { color: var(--ink); font-size: 88px; }
  .product-name .tm { display: inline; font-size: 26px; vertical-align: 48px; letter-spacing: 0; }

  .blend-pill {
    position: absolute; left: 54px; top: 360px; width: 424px; height: 42px;
    border-radius: 21px;
    background: linear-gradient(180deg, var(--green-light), var(--green) 55%, var(--green-deep));
    border: 2px solid #9fb7ad;
    color: #fff; text-align: center;
    font-family: "Ubuntu", sans-serif; font-weight: 700; font-size: 27px; line-height: 37px;
  }

  .benefits {
    position: absolute; left: 58px; top: 424px; list-style: none;
    font-family: "Ubuntu", sans-serif; font-weight: 500; font-size: 30px; line-height: 31px;
    color: var(--green);
  }
  .benefits li { position: relative; padding-left: 24px; margin-bottom: 11px; }
  .benefits li::before {
    content: ""; position: absolute; left: 0; top: 10px;
    width: 12px; height: 12px; border-radius: 50%; background: var(--green);
  }

  .fruit-art {
    position: absolute; left: 258px; top: 428px; width: 228px; height: 150px;
    border-radius: 40% 45% 35% 40%;
    background: radial-gradient(ellipse at 55% 55%, #e0313a 0%, #c61f2a 45%, #7fa65a 75%, rgba(255,255,255,0) 100%);
  }

  .claims {
    position: absolute; left: 519px; top: 0; width: 107px; height: 560px;
    background: var(--green);
  }
  .claim {
    position: absolute; left: 0; width: 107px; text-align: center;
    font-family: "Oswald", sans-serif; font-weight: 400; font-size: 26px; line-height: 24px;
    color: #fff; text-transform: uppercase; letter-spacing: -0.5px;
  }
  .claim svg { display: block; margin: 0 auto 5px; }
  .claim-rule {
    position: absolute; left: 12px; width: 85px; height: 2px; background: #5fb692;
  }

  .count-badge {
    position: absolute; left: 519px; top: 502px; width: 107px; height: 107px;
  }

  .flavor-band {
    position: absolute; left: 0; top: 615px; width: 660px; height: 50px;
    background: var(--green);
    color: #fff; font-family: "Ubuntu", sans-serif; font-weight: 700;
    font-size: 25px; line-height: 50px; padding-left: 88px;
  }
</style>
</head>
<body>
  <section class="label">
    <p class="brand-name">RT Balden's</p>
    <h1 class="product-name">
      <span>MEADOW</span>
      <span>TWIST</span>
      <span class="dark">CHEWS<span class="tm">™</span></span>
    </h1>

    <div class="blend-pill">Super Greens Blend</div>

    <ul class="benefits">
      <li>Energy</li>
      <li>Digestion</li>
      <li>Immune<br>Support</li>
    </ul>

    <div class="fruit-art" role="img" aria-label="Photo of fresh raspberries with green leaves"></div>

    <aside class="claims">
      <div class="claim" style="top:80px">
        <svg width="28" height="28" viewBox="0 0 32 32"><circle cx="16" cy="16" r="16" fill="#fff"/><path d="M12 7c0 6 8 12 8 18M20 7c0 6-8 12-8 18M13 12h6M13 20h6" stroke="var(--green)" stroke-width="1.8" fill="none"/></svg>
        Non<br>GMO
      </div>
      <div class="claim-rule" style="top:174px"></div>

      <div class="claim" style="top:188px">
        <svg width="28" height="28" viewBox="0 0 32 32"><circle cx="16" cy="16" r="16" fill="#fff"/><path d="M16 24c-6 0-8-6-8-11 5 0 8 3 8 11zM16 24c6 0 8-6 8-11-5 0-8 3-8 11z" fill="var(--green)"/></svg>
        Vegan<br>Friendly
      </div>
      <div class="claim-rule" style="top:283px"></div>

      <div class="claim" style="top:294px">
        <svg width="28" height="28" viewBox="0 0 32 32"><circle cx="16" cy="16" r="16" fill="#fff"/><path d="M16 25V13M16 17c-5 0-6-5-6-8 4 0 6 3 6 8zM16 17c5 0 6-5 6-8-4 0-6 3-6 8z" stroke="var(--green)" stroke-width="1.8" fill="none"/></svg>
        Plant<br>Based
      </div>
      <div class="claim-rule" style="top:390px"></div>

      <div class="claim" style="top:402px">
        <svg width="28" height="28" viewBox="0 0 32 32"><circle cx="16" cy="16" r="16" fill="#fff"/><path d="M16 26V8M16 12l-4-3M16 12l4-3M16 17l-5-3M16 17l5-3M16 22l-5-3M16 22l5-3" stroke="var(--green)" stroke-width="2" fill="none" stroke-linecap="round"/></svg>
        Gelatin<br>Free
      </div>
    </aside>

    <svg class="count-badge" viewBox="0 0 107 107" aria-label="60 Gummies, Dietary Supplement">
      <circle cx="53.5" cy="53.5" r="53" fill="#fff"/>
      <circle cx="53.5" cy="53.5" r="49" fill="var(--green)"/>
      <circle cx="53.5" cy="53.5" r="43" fill="var(--silver)"/>
      <clipPath id="badge-inner"><circle cx="53.5" cy="53.5" r="39"/></clipPath>
      <g clip-path="url(#badge-inner)">
        <rect x="0" y="0" width="107" height="107" fill="var(--green)"/>
        <path d="M10 60 Q53.5 52 97 60 V0 H10z" fill="#fff"/>
      </g>
      <text x="53.5" y="43" text-anchor="middle" font-family="Ubuntu, sans-serif" font-weight="700" font-size="17" fill="var(--berry)">60</text>
      <text x="53.5" y="53" text-anchor="middle" font-family="Ubuntu, sans-serif" font-weight="700" font-size="8" fill="var(--ink)">GUMMIES</text>
      <text x="53.5" y="68" text-anchor="middle" font-family="Ubuntu, sans-serif" font-weight="500" font-size="7.5" fill="#fff">Dietary</text>
      <text x="53.5" y="77" text-anchor="middle" font-family="Ubuntu, sans-serif" font-weight="500" font-size="7.5" fill="#fff">Supplement</text>
    </svg>

    <div class="flavor-band">Raspberry Flavor Gummies</div>
  </section>
</body>
</html>
```